FLYERENTWURF  für Make up Ausbildung
FLYERENTWURF für Make up Ausbildung
Zielgruppe
friseure die sich weiterbilden wollen
Aufgabenstellung
zu entwerfen ist ein doppelseitiger flyer in A4, zweimal gefalten.
außenseite:
erste spalte/deckblatt:
das logo (im anhang)
schriftzug: mira beauty schule
eventuell bild kussmund, wenn rechte vorhanden.
zweite spalte/hinterseite:
zahlungsbedingungen (text wird noch beigefügt)
dritte spalte:
personenbild (anhang)
personenbeschreibung (text wird noch beigefügt)
innenseite:
text aus anhang

```html
<!DOCTYPE html>
<html lang="de">
<head>
<meta charset="utf-8">
<title>mira beauty schule – Flyer</title>
<link rel="stylesheet" href="https://fonts.googleapis.com/css2?family=Open+Sans:wght@400;600;700&display=swap">
<style>
  :root{
    --page:#e4e4e4;
    --navy:#0c1424;
    --band:#9ccbf1;
    --band-deep:#5f9fd8;
    --head:#8fc6f2;
    --pink:#e07aa8;
    --text:#d9dde6;
    --cover-top:#2a3590;
    --cover-bottom:#8ea6e6;
    --title:#d8472a;
    --hair:#8a1f24;
    --hair-light:#a82a30;
  }
  *{box-sizing:border-box;margin:0;padding:0}
  html,body{width:1200px;height:900px;overflow:hidden;background:var(--page)}
  body{position:relative;font-family:"Open Sans",Arial,sans-serif;color:var(--text)}

  .spread{position:absolute;left:280px;width:640px;height:435px;background:var(--navy);overflow:hidden}
  .spread--outside{top:10px}
  .spread--inside{top:455px}

  .band{position:absolute;left:0;width:640px;height:40px;z-index:3}
  .band--top{top:0}
  .band--bottom{bottom:0}

  .text-block{position:absolute;z-index:2;font-size:6.8px;line-height:8.6px}
  .text-block p{margin-bottom:4px}
  .heading{color:var(--head);font-weight:700;font-size:10px;line-height:12px;margin-bottom:8px}
  .subhead{color:var(--pink);font-weight:700;font-size:7.2px;margin:6px 0 2px}
  .bullets{list-style:none}
  .bullets li::before{content:"• "}
  .bullets li.indent{padding-left:6px}
  .bullets li.indent::before{content:""}
  .dates{border-collapse:collapse;font-size:6.8px;line-height:8.4px}
  .dates td{padding:0 10px 0 0}

  /* outside */
  .portrait{position:absolute;z-index:1;left:22px;top:48px;width:92px;height:126px;background:linear-gradient(160deg,#3a2a24,#c59a86 55%,#e8d6cc)}
  .figure{position:absolute;z-index:1;left:148px;top:150px;width:72px;height:285px;
    background:linear-gradient(180deg,rgba(138,31,36,0) 0,var(--hair-light) 18%,var(--hair) 60%,rgba(138,31,36,.55) 100%);
    border-radius:36px 36px 0 0}
  .person-text{left:10px;top:182px;width:132px}
  .payment-text{left:218px;top:40px;width:190px}
  .cover{position:absolute;left:427px;top:0;width:213px;height:435px;background:linear-gradient(175deg,var(--cover-top),#4a5fc0 45%,var(--cover-bottom))}
  .cover-name{position:absolute;left:30px;top:70px;display:flex;align-items:center;gap:8px;color:#ffffff;font-weight:700;font-size:15px}
  .cover-name .dot{width:10px;height:10px;border-radius:50%;background:#ffffff}
  .lips{position:absolute;right:0;top:140px;width:90px;height:60px;background:radial-gradient(ellipse at 70% 50%,#9a4f6a 0,#7a5a92 50%,rgba(122,90,146,0) 75%)}
  .cover-title{position:absolute;left:40px;top:250px;color:var(--title);font-weight:700;font-size:27px;line-height:28px}

  /* inside */
  .silhouette{position:absolute;z-index:1;left:60px;top:60px;width:260px;height:360px;
    background:radial-gradient(ellipse at 35% 40%,#3c4866 0,#2a3550 45%,rgba(42,53,80,0) 72%)}
  .col{width:190px}
  .col--1{left:12px;top:48px}
  .col--2{left:225px;top:30px}
  .col--3{left:437px;top:30px}
  .footnote{position:absolute;z-index:2;left:12px;bottom:44px;width:100px;font-size:4.6px;line-height:5.6px}
</style>
</head>
<body>

<section class="spread spread--outside" aria-label="Außenseite">
  <div class="cover">
    <div class="cover-name"><span class="dot"></span>mira beauty schule</div>
    <div class="lips" role="img" aria-label="Foto eines Kussmunds"></div>
    <h1 class="cover-title">mira<br>beauty<br>schule</h1>
  </div>

  <div class="portrait" role="img" aria-label="Porträtfoto der Kursleiterin"></div>
  <div class="figure" role="img" aria-label="Illustration einer Frau mit wehendem roten Haar"></div>

  <div class="person-text text-block">
    <h2 class="heading">zur person</h2>
    <p>Seit über zehn Jahren arbeite ich als Visagistin für Film, Fernsehen, Mode und Fotografie. Nach meiner Ausbildung zur Friseurin habe ich mich auf Make-up spezialisiert und zahlreiche Shows und Shootings betreut. Heute gebe ich mein Wissen in kleinen Gruppen weiter, praxisnah, persönlich und mit viel Freude an kreativen Ideen.</p>
  </div>

  <div class="payment-text text-block">
    <h2 class="heading">zahlungsbedingungen</h2>
    <p>Die Kursgebühr ist bis spätestens zwei Wochen vor Kursbeginn auf das angegebene Konto zu überweisen. Mit der Anmeldung wird eine Anzahlung von 30 Prozent fällig. Bei Stornierung bis vier Wochen vor Beginn wird die Anzahlung abzüglich einer Bearbeitungsgebühr erstattet. Danach ist eine Rückerstattung leider nicht mehr möglich. Ein Ersatzteilnehmer kann jederzeit genannt werden. Alle Materialien sind im Preis enthalten. Änderungen der Termine bleiben vorbehalten.</p>
  </div>

  <svg class="band band--top" viewBox="0 0 640 40" preserveAspectRatio="none" aria-hidden="true">
    <path d="M0 0H640V14C480 2 320 30 160 22 90 18 40 10 0 14Z" fill="var(--band)"/>
  </svg>
  <svg class="band band--bottom" viewBox="0 0 640 40" preserveAspectRatio="none" aria-hidden="true">
    <path d="M0 30C160 16 330 14 480 22 560 26 610 18 640 12V40H0Z" fill="var(--band)"/>
  </svg>
</section>

<section class="spread spread--inside" aria-label="Innenseite">
  <div class="silhouette" role="img" aria-label="Silhouette einer Frau mit fliegendem Haar"></div>

  <div class="col col--1 text-block">
    <h2 class="heading">basic education teil 1</h2>
    <p>in diesem workshop wird basiswissen vermittelt, mit dem jeder friseur professionell sein beauty-salonprogramm abrunden und das sortiment seiner dienstleistungen erweitern kann.</p>
    <h3 class="subhead">inhalte auf einen blick:</h3>
    <ul class="bullets">
      <li>produktwissen</li>
      <li>gesichtsvermessungen</li>
      <li>optimierung der gesichtsformen</li>
      <li>augenmakeups</li>
      <li>makeup für verschiedene augenformen</li>
      <li>augen-makeup für brillenträgerinnen</li>
      <li>tages-makeup</li>
      <li>abend-makeup</li>
      <li>special-makeup (wimpern kleben, auf</li>
      <li class="indent">bringen von glitter und accessoires)</li>
    </ul>
    <h3 class="subhead">termine</h3>
    <table class="dates">
      <tr><td>so</td><td>08.05.2011</td><td>10-18 uhr</td></tr>
      <tr><td>mo</td><td>09.05.2011</td><td>10-14 uhr</td></tr>
      <tr><td>so</td><td>15.05.2011</td><td>10-18 uhr</td></tr>
      <tr><td>mo</td><td>16.05.2011</td><td>10-14 uhr</td></tr>
      <tr><td>so</td><td>22.05.2011</td><td>10-18 uhr</td></tr>
      <tr><td>mo</td><td>23.05.2011</td><td>10-14 uhr</td></tr>
      <tr><td>so</td><td>29.05.2011</td><td>10-18 uhr</td></tr>
      <tr><td>mo</td><td>30.05.2011</td><td>10-14 uhr</td></tr>
    </table>
    <h3 class="subhead">voraussetzungen</h3>
    <p>dieser kurs ist geeignet für einsteiger und für alle, die vorhandenes wissen auffrischen oder vertiefen wollen.</p>
    <h3 class="subhead">kosten</h3>
    <p>€ 990 exkl. mwst.<br>anmeldung<br>bis 01.03.2011<br>mira@lockenglanzsalon.at oder 01 234 56 78</p>
  </div>

  <div class="col col--2 text-block">
    <h2 class="heading">junior makeup artist teil 2</h2>
    <p>junior makeup artists, die diesen kurs absolviert haben, sind in der lage, makeup- und typberatung, foto- und anti-aging-makeup anzubieten. die inhalte befassen sich noch detaillierter als im ersten teil mit farben und formen beim schminken und die techniken werden von der beratung bis zur umsetzung trainiert.</p>
    <h3 class="subhead">inhalte auf einen blick:</h3>
    <ul class="bullets">
      <li>haut</li>
      <li>anti-aging-makeup</li>
      <li>foto-makeup</li>
      <li>schwarz/weiß foto-makeup</li>
      <li>männer-makeup</li>
      <li>typberatung</li>
      <li>makeup beratung</li>
      <li>braut-makeup</li>
    </ul>
    <h3 class="subhead">termine</h3>
    <table class="dates">
      <tr><td>so</td><td>10.07.2011</td><td>10-18 uhr</td></tr>
      <tr><td>mo</td><td>11.07.2011</td><td>10-14 uhr</td></tr>
      <tr><td>so</td><td>17.07.2011</td><td>10-18 uhr</td></tr>
      <tr><td>mo</td><td>18.07.2011</td><td>10-14 uhr</td></tr>
      <tr><td>so</td><td>24.07.2011</td><td>10-18 uhr</td></tr>
      <tr><td>mo</td><td>25.07.2011</td><td>10-14 uhr</td></tr>
      <tr><td>so</td><td>31.07.2011</td><td>10-18 uhr</td></tr>
      <tr><td>mo</td><td>01.08.2011</td><td>10-14 uhr</td></tr>
    </table>
    <h3 class="subhead">voraussetzungen</h3>
    <p>dieser kurs ist geeignet für friseure mit basiswissen, talentierte quereinsteiger und teilnehmer des ersten kurses. makeup basics teilnehmer von makeup basics erhalten nach diesem kurs auch das junior makeup artist diplom.</p>
    <h3 class="subhead">kosten</h3>
    <p>€ 990 exkl. mwst.<br>anmeldung<br>bis 01.05.2011<br>mira@lockenglanzsalon.at oder 01 234 56 78</p>
  </div>

  <div class="col col--3 text-block">
    <h2 class="heading">creative makeup teil 3</h2>
    <p>ob film, theater, fashion shows und fotoshootings – du lernst die looks verschiedener epochen zu schminken aber auch abzuwandeln. in diesem workshop nehmen wir uns besonders viel zeit, techniken zu perfektionieren und deiner makeup-kunst eine individuelle note zu geben.</p>
    <h3 class="subhead">inhalte auf einen blick:</h3>
    <ul class="bullets">
      <li>epochen-makeup (20er bis 90er jahre)</li>
      <li>verschiedene kulturen/historische makeups (geisha, orientalisches makeup,...)</li>
      <li>geschichte des makeup</li>
      <li>laufsteg makeup (konzepterstellung, makeup-design, planung)</li>
      <li>x-treme makeup/phantasie-makeup</li>
    </ul>
    <h3 class="subhead">termine</h3>
    <table class="dates">
      <tr><td>so</td><td>11.09.2011</td><td>10-18 uhr</td></tr>
      <tr><td>mo</td><td>12.09.2011</td><td>10-14 uhr</td></tr>
      <tr><td>so</td><td>18.09.2011</td><td>10-18 uhr</td></tr>
      <tr><td>mo</td><td>19.09.2011</td><td>10-14 uhr</td></tr>
      <tr><td>so</td><td>25.09.2011</td><td>10-18 uhr</td></tr>
      <tr><td>mo</td><td>26.09.2011</td><td>10-14 uhr</td></tr>
      <tr><td>so</td><td>02.10.2011</td><td>10-18 uhr</td></tr>
      <tr><td>mo</td><td>03.10.2011</td><td>10-14 uhr</td></tr>
    </table>
    <h3 class="subhead">voraussetzungen</h3>
    <p>dieser kurs ist geeignet für kreative künstler mit vorbildung und rundet die ausbildung für teilnehmer von teil 1 und 2 makeup basics und junior makeup artist perfekt ab. der kurs endet mit einer schriftlichen und praktischen prüfung, die auch die ersten beiden kurse beurteilt. nach bestandener prüfung ein visagistendiplom.</p>
    <h3 class="subhead">kosten</h3>
    <p>€ 990 exkl. mwst.<br>anmeldung<br>bis 01.07.2011<br>mira@lockenglanzsalon.at oder 01 234 56 78</p>
  </div>

  <p class="footnote">bei anmeldung für alle drei kurse bis 01.03.2011 erhältst du 10% rabatt auf den gesamtpreis</p>

  <svg class="band band--top" viewBox="0 0 640 40" preserveAspectRatio="none" aria-hidden="true">
    <path d="M0 0H640V10C520 4 380 22 250 18 150 14 60 8 0 12Z" fill="var(--band)"/>
  </svg>
  <svg class="band band--bottom" viewBox="0 0 640 40" preserveAspectRatio="none" aria-hidden="true">
    <path d="M0 32C150 26 300 14 450 18 540 20 600 14 640 10V40H0Z" fill="var(--band)"/>
    <path d="M0 34C160 28 310 17 460 21 550 23 605 17 640 14" fill="none" stroke="var(--band-deep)" stroke-width="1.2"/>
  </svg>
</section>

</body>
</html>
```